依頼詳細
タワーマンションの理事長にチラシを配布しようと思っています。そのチラシデザイン制作をお願いします。見る人が思わず参加したくなるようなインパクトのあるデザインをお願いします。
記載項目
社名:株式会社MN建築設計/電話:06-4827-3956/URL:http://mn-kenchiku.co.jp
サイズ
A4
ページ数
両面
希望イメージ
シンプル 複雑
単色 カラフル
暗い 明るい
日常 高級
遊び心 厳粛
未来的 伝統的
女性的 男性的

弊社のイメージカラーに合っていたこと、内容が見やすくて分かりやすかった為

このたびは短い期間でありながらもご参加いただきありがとうございました。
皆様の提案は全て良かったので選定に苦慮いたしました。今回選定されなかったご提案者様は残念な結果となりましたが、今後もご提案をお願いするときには是非参加くださいますようお願い申し上げます。

```html
<!DOCTYPE html>
<html lang="ja">
<head>
<meta charset="UTF-8">
<title>タワーマンション管理組合 交流会</title>
<link href="https://fonts.googleapis.com/css2?family=Noto+Sans+JP:wght@400;500;700;900&family=M+PLUS+Rounded+1c:wght@700;800&display=swap" rel="stylesheet">
<style>
  :root{
    --navy:#13306e;
    --blue:#1f5fbf;
    --sky-top:#2a63c4;
    --sky-mid:#8cc2ec;
    --sky-low:#d9eefb;
    --yellow:#ffe000;
    --red:#e0231e;
    --green:#3f9c3a;
    --ink:#1b1b1b;
    --paper:#ffffff;
    --line:#1f5fbf;
  }
  *{margin:0;padding:0;box-sizing:border-box}
  html,body{width:856px;height:1200px;overflow:hidden;background:#fff}
  body{font-family:"Noto Sans JP",sans-serif;color:var(--ink)}
  .flyer{position:relative;width:856px;height:1200px;overflow:hidden;
    background:linear-gradient(180deg,var(--sky-top) 0%,var(--sky-mid) 28%,var(--sky-low) 46%,#fff 56%,#fff 100%)}
  .tower-visual{position:absolute;left:270px;top:40px;width:330px;height:530px;
    background:linear-gradient(180deg,#c8d6e6 0%,#8ea6bf 45%,#6e8aa6 80%,#3f8a3c 90%,#2e7a2e 100%);
    border-radius:6px 6px 0 0;opacity:.9}
  .eyebrow{position:absolute;top:30px;left:0;width:100%;text-align:center;color:#fff;
    font-weight:900;font-size:38px;letter-spacing:2px;text-shadow:0 2px 4px rgba(0,0,0,.35)}
  .title{position:absolute;top:78px;left:0;width:100%;text-align:center;
    font-family:"M PLUS Rounded 1c",sans-serif;font-weight:800;font-size:170px;line-height:1;
    color:var(--yellow);-webkit-text-stroke:7px var(--navy);paint-order:stroke fill;letter-spacing:6px}
  .tagline{position:absolute;top:250px;left:160px;width:536px;height:50px;border-radius:25px;
    background:var(--blue);color:#fff;font-weight:700;font-size:31px;text-align:center;line-height:50px;
    letter-spacing:3px;border:3px solid #fff}
  .bubble{position:absolute;background:#fff;border:3px solid var(--blue);border-radius:50%;
    display:flex;align-items:center;justify-content:center;text-align:center;
    font-family:"M PLUS Rounded 1c",sans-serif;font-weight:800;color:var(--red);line-height:1.25}
  .bubble small{display:block;font-size:17px;color:var(--navy)}
  .b1{left:26px;top:130px;width:150px;height:140px;font-size:24px}
  .b2{left:672px;top:112px;width:160px;height:150px;font-size:24px}
  .b3{left:18px;top:290px;width:150px;height:110px;font-size:25px}
  .b4{left:668px;top:310px;width:160px;height:105px;font-size:25px}
  .b5{left:14px;top:415px;width:185px;height:115px;font-size:22px}
  .b6{left:650px;top:435px;width:180px;height:105px;font-size:24px}

  .notice{position:absolute;left:40px;top:560px;width:400px;height:135px;background:#fff;
    border:2px solid var(--line);padding:8px 12px;font-size:12.5px;line-height:1.55}
  .notice h3{color:var(--red);font-size:15px;font-weight:700;margin-bottom:3px}
  .detail{position:absolute;left:40px;display:flex;align-items:flex-start;gap:16px}
  .detail .label{background:var(--blue);color:#fff;font-weight:700;font-size:24px;
    width:88px;height:42px;line-height:42px;text-align:center;border-radius:4px}
  .detail .value{font-weight:900;font-size:34px;line-height:1.2;color:var(--navy)}
  .detail .sub{display:block;font-weight:700;font-size:22px;color:var(--ink)}
  .detail .addr{display:block;font-weight:500;font-size:14px;color:var(--ink);margin-top:2px}
  .d-date{top:712px}.d-cap{top:800px}.d-venue{top:858px}
  .deadline{position:absolute;left:40px;top:945px;width:560px;height:54px;background:var(--red);
    color:#fff;font-weight:900;font-size:32px;line-height:54px;text-align:center;border-radius:27px;letter-spacing:1px}

  .program{position:absolute;left:470px;top:565px;width:350px;height:330px;background:#fff;
    border:3px solid var(--line);border-radius:10px;padding:16px 20px}
  .program h2{color:var(--blue);font-size:26px;font-weight:900;margin-bottom:10px}
  .session{margin-bottom:14px}
  .session .time{color:var(--navy);font-weight:700;font-size:20px}
  .session .name{font-weight:700;font-size:20px}
  .session .name em{font-style:normal;font-size:15px}
  .session p{font-size:13px;line-height:1.55;margin-top:3px}

  .contact{position:absolute;left:636px;top:915px;width:184px;height:185px;background:#fff;
    border:3px solid var(--line);border-radius:10px;padding:14px 12px;text-align:center;font-weight:700}
  .contact .lead{font-size:15px}
  .contact .big{font-size:28px;color:var(--red);font-weight:900;margin:4px 0}
  .contact .note{font-size:15px;color:var(--blue)}
  .contact svg{display:block;margin:6px auto 0}

  .host{position:absolute;left:0;top:1140px;width:100%;height:60px;background:var(--blue);
    color:#fff;text-align:center;font-size:28px;font-weight:700;line-height:60px;letter-spacing:2px}
</style>
</head>
<body>
<div class="flyer">
  <div class="tower-visual" role="img" aria-label="青空に向かってそびえるタワーマンションと足元の緑の木々の写真"></div>

  <p class="eyebrow">タワーマンション管理組合</p>
  <h1 class="title">交流会</h1>
  <p class="tagline">管理組合の自立を目指す</p>

  <div class="bubble b1"><span><small>他の</small>マンションは<br>どう？</span></div>
  <div class="bubble b2"><span><small>分譲</small>マンションの<br>未来を<br>考える</span></div>
  <div class="bubble b3"><span>管理費の<br>上げ？</span></div>
  <div class="bubble b4"><span>修繕費が<br>高くない？</span></div>
  <div class="bubble b5"><span>理事の<br>なり手がいないが<br>どうする？</span></div>
  <div class="bubble b6"><span>民泊問題は<br>どうする？</span></div>

  <section class="notice">
    <h3>新型コロナウイルス対策について</h3>
    <p>交流会では新型コロナウイルスの感染予防対策として、入口での手指消毒と検温、マスクの着用をお願いしております。会場は定期的に換気を行い、座席の間隔を広く取って開催いたします。体調のすぐれない方はご参加をお控えください。ご理解とご協力をお願いいたします。</p>
  </section>

  <div class="detail d-date"><span class="label">日時</span>
    <span class="value">2022年7月31日(日)<span class="sub">10:00～12:00</span></span></div>
  <div class="detail d-cap"><span class="label">定員</span>
    <span class="value">先着15名様</span></div>
  <div class="detail d-venue"><span class="label">会場</span>
    <span class="value">グランタワー天王寺<span class="addr">大阪府大阪市阿倍野区旭町3丁目8番12号</span></span></div>

  <p class="deadline">申込締切：2022年7月19日(日)</p>

  <section class="program">
    <h2>交流会プログラム</h2>
    <div class="session">
      <p class="time">10:00～10:40</p>
      <p class="name">第1部 意見交流会<em>（会員参加型）</em></p>
      <p>他のマンションの方々と、課題を共有し、解決策を探ります。</p>
    </div>
    <div class="session">
      <p class="time">10:50～11:50</p>
      <p class="name">第2部 修繕工事の進め方</p>
      <p>講師 三宅（一級建築士）</p>
    </div>
  </section>

  <section class="contact">
    <p class="lead">お問合せ・お申込みは</p>
    <p class="big">裏面を</p>
    <p class="lead">ご覧ください</p>
    <p class="note">●メール・FAXにて受付中！</p>
    <svg width="40" height="28" viewBox="0 0 40 28" aria-hidden="true"><path d="M2 14h28M20 4l12 10-12 10" fill="none" stroke="#e0231e" stroke-width="5" stroke-linecap="round" stroke-linejoin="round"/></svg>
  </section>

  <footer class="host">主催：マンション管理組合交流会</footer>
</div>
</body>
</html>
```